Business is called "Pelton Ledger". Accounting and tax services.

I need a flyer for my new business "Pelton Ledger". I am an individual accountant working for himself on the Sunshine Coast in Queensland Australia. I would like to see designs that communicate reliability and trust. I believe my point of difference is that I am always available to my clients and I will cap my number of clients to ensure I can service them properly. Accountants in general seem to have a bad reputation for not responding to clients in a timely fashion, whether by email or phone. This is where I intend to differentiate myself. I have included my business card for ideas on colour and for contact information. I have also included some logo's that should go on the flyer. With the QLA logo, the words "Pelton Ledger is a QLA Business" needs to be written either above, below or to the right hand side (as per the business card).

Target Market(s)

Small business owners and individuals requiring taxation and financials

Industry/Entity Type

Public Accounting

Font styles to use
Serif

Requirements
Must have
• Supplied logo's, accounting style pictures etc
Services: Small Business Taxation
Company & Trust Tax Returns
Rental Property Returns
Capital Gains Tax
Individual Tax Returns
BAS and IAS lodgements
Nice to have
• Needs to convey a sense of being reliable and responds to clients quickly.
Should not have
• My name

```html
<!DOCTYPE html>
<html lang="en">
<head>
<meta charset="utf-8">
<title>Pelton Ledger – Flyer Cards</title>
<link rel="stylesheet" href="https://fonts.googleapis.com/css2?family=Montserrat:wght@500;600&family=Hind:wght@300;400&family=PT+Serif:wght@700&display=swap">
<style>
  :root {
    --teal-light: #2ab896;
    --teal-deep: #1f9d80;
    --ink-green: #1a6b58;
    --ink-dark: #2a2a2a;
    --mint-band: #eaf6f3;
    --white: #ffffff;
    --badge-grey: #d9e4e0;
  }
  * { box-sizing: border-box; margin: 0; padding: 0; }
  html, body { width: 1200px; height: 1053px; overflow: hidden; background: var(--white); }
  .canvas { position: relative; width: 1200px; height: 1053px; }

  /* Front card */
  .card-front {
    position: absolute; left: 202px; top: 282px; width: 348px; height: 490px;
    background: linear-gradient(135deg, var(--teal-light) 0%, var(--teal-deep) 100%);
    color: var(--white); text-align: center;
  }
  .calculator-art {
    position: absolute; left: 120px; top: 109px; width: 108px; height: 153px;
    border-radius: 7px; background: rgba(255,255,255,0.16);
  }
  .front-mark {
    position: absolute; left: 156px; top: 388px; width: 36px; height: 36px;
    border: 1.5px solid var(--white); border-radius: 50%;
  }
  .front-name {
    position: absolute; left: 0; right: 0; top: 430px;
    font: 500 12px/1 "Montserrat", sans-serif; letter-spacing: 4px;
  }
  .front-contact {
    position: absolute; left: 0; right: 0; top: 445px;
    font: 300 14px/14px "Hind", sans-serif;
  }

  /* Back card */
  .card-back {
    position: absolute; left: 652px; top: 282px; width: 348px; height: 490px;
    background: linear-gradient(135deg, var(--teal-light) 0%, var(--teal-deep) 100%);
  }
  .card-back-inner {
    position: absolute; left: 16px; top: 17px; width: 315px; height: 456px;
    background: var(--white); overflow: hidden;
  }
  .brand-mark {
    position: absolute; left: 129px; top: 18px; width: 56px; height: 56px;
    border: 2px solid var(--ink-dark); border-radius: 50%;
  }
  .brand-name {
    position: absolute; left: 0; right: 0; top: 84px; text-align: center;
    font: 600 16px/1 "Montserrat", sans-serif; letter-spacing: 5px; color: var(--ink-dark);
  }
  .services {
    position: absolute; left: 0; top: 114px; width: 315px; height: 206px;
    background: var(--mint-band); list-style: none; padding-top: 14px;
  }
  .service {
    display: flex; align-items: center; height: 30.5px;
    font: 300 18px/1 "Hind", sans-serif; color: var(--ink-green);
  }
  .service svg { width: 24px; height: 24px; margin: 0 18px 0 21px; flex: none; }
  .phone {
    position: absolute; left: 0; right: 0; top: 334px;
    display: flex; justify-content: center; align-items: center; gap: 12px;
    font: 300 28px/1 "Hind", sans-serif; color: var(--ink-green); letter-spacing: -0.5px;
  }
  .phone svg { width: 18px; height: 26px; }
  .partners { position: absolute; left: 0; top: 392px; width: 315px; height: 60px; }
  .qla-note {
    position: absolute; left: 28px; top: 0; width: 84px;
    font: 700 9px/10px "PT Serif", serif; color: var(--ink-dark);
  }
  .qla-name {
    position: absolute; left: 28px; top: 28px; display: flex; align-items: center; gap: 6px;
    font: 300 16px/1 "Hind", sans-serif; color: var(--ink-green);
  }
  .qla-name .square { width: 11px; height: 11px; background: var(--ink-green); }
  .ledgra {
    position: absolute; left: 138px; top: 20px; display: flex; align-items: center; gap: 6px;
    font: 300 16px/1 "Hind", sans-serif; color: var(--ink-green);
  }
  .ledgra .dot { width: 11px; height: 11px; border-radius: 50%; background: var(--ink-green); }
  .agent-badge {
    position: absolute; left: 256px; top: 4px; width: 32px; height: 32px;
    border-radius: 50%; background: var(--badge-grey);
  }
  .agent-id {
    position: absolute; left: 240px; top: 40px; width: 64px; text-align: center;
    font: 400 7px/8px "Hind", sans-serif; color: var(--ink-dark);
  }
</style>
</head>
<body>
<div class="canvas">

  <section class="card-front">
    <div class="calculator-art" role="img" aria-label="Outline calculator illustration"></div>
    <div class="front-mark"></div>
    <div class="front-name">PELTON LEDGER</div>
    <div class="front-contact">www.peltonledger.com.au<br>hello@peltonledger.com.au</div>
  </section>

  <section class="card-back">
    <div class="card-back-inner">
      <div class="brand-mark"></div>
      <div class="brand-name">PELTON LEDGER</div>

      <ul class="services">
        <li class="service">
          <svg viewBox="0 0 24 24" fill="none" stroke="#1a6b58" stroke-width="1.6"><path d="M5 18l2-5 9-9 3 3-9 9z"/><path d="M3 22h18"/></svg>
          Small Business Taxation</li>
        <li class="service">
          <svg viewBox="0 0 24 24" fill="#1a6b58"><rect x="5" y="14" width="2" height="6"/><rect x="9" y="11" width="2" height="9"/><rect x="13" y="12" width="2" height="8"/><rect x="17" y="8" width="2" height="12"/><path d="M3 22h19v1H3zM3 2h1v20H3z"/><path d="M5 12l5-4 3 2 6-6" stroke="#1a6b58" stroke-width="1.2" fill="none"/></svg>
          Company &amp; Trust Tax Returns</li>
        <li class="service">
          <svg viewBox="0 0 24 24" fill="none" stroke="#1a6b58" stroke-width="1.6"><rect x="3" y="3" width="18" height="18"/><circle cx="12" cy="12" r="4.5" fill="#1a6b58"/></svg>
          Rental Property Returns</li>
        <li class="service">
          <svg viewBox="0 0 24 24" fill="#1a6b58"><rect x="2" y="4" width="5" height="17"/><rect x="8" y="4" width="5" height="17"/><rect x="14" y="4" width="5" height="17" transform="rotate(-10 16 12)"/></svg>
          Capital Gains Tax</li>
        <li class="service">
          <svg viewBox="0 0 24 24" fill="none" stroke="#1a6b58" stroke-width="1.3"><rect x="5" y="4" width="14" height="18" rx="1"/><path d="M8 9h8M8 12h8M8 15h8M8 18h5"/><rect x="10" y="2" width="4" height="3" fill="#1a6b58"/></svg>
          Individual Tax Returns</li>
        <li class="service">
          <svg viewBox="0 0 24 24" fill="#1a6b58"><rect x="2" y="7" width="20" height="14" rx="2"/><path d="M9 7V4h6v3" stroke="#1a6b58" stroke-width="1.5" fill="none"/><rect x="11" y="12" width="2" height="2" fill="#eaf6f3"/></svg>
          BAS and IAS lodgements</li>
      </ul>

      <div class="phone">
        <svg viewBox="0 0 18 26" fill="#1a6b58"><path d="M4 1l3 1-1 6-2 1c0 4 2 8 5 11l2-1 4 4-2 2C7 25 1 15 1 5z"/></svg>
        0412 555 830
      </div>

      <div class="partners">
        <div class="qla-note">Pelton Ledger is a QLA Business</div>
        <div class="qla-name">QLA<span class="square"></span></div>
        <div class="ledgra"><span class="dot"></span>Ledgra</div>
        <div class="agent-badge"></div>
        <div class="agent-id">Tax agent<br>10293847</div>
      </div>
    </div>
  </section>

</div>
</body>
</html>
```